Innovative Healthcare Technology Company needs a Business Card Design

We are in need of an innovative business card design for a new healthcare software company called "Lumenwise Data Partners". We develop software that creates medical assessment applications and mobile e-learning prevention services to reduce risk behaviors in adolescent and young adults. Our initial product, the "KESTREL App", conducts a tailored sexual risk assessment and provides a doctor with an insightful patient report to improve sexual risk counseling and ultimately reduce unintended pregnancy, STDs, etc.

We would like the design to incorporate our logo and branding colors (attached) in an innovative and creative manner. The final design should communicate professionalism and healthcare innovation. Our tag line is "Foresight is the best care" (doesn't necessarily need to be included) and our target audience is doctors, medical directors, and medical business administrators. Please visit our website for additional info ourbrightmarq.com. Be creative and we look forward to seeing your designs!

Target Market(s)

healthcare - doctors, medical directors and medical business administrators

Industry/Entity Type

Healthcare

Contact Information for Business Card

We would like the design to incorporate our logo and branding colors (attached) in an innovative and creative manner. The final design should communicate professionalism and healthcare innovation. Our tag line is "Foresight is the best care" (doesn't necessarily need to be included)

Font styles to use
Other font styles liked:
• quicksand

Requirements
Must have
• our logo and brand colors
• Name, (Mara Feldhovenik, PhD)
• Email (drmara@ourbrightmarq.com)
• phone (555.283.9170)
• Website (ourbrightmarq.com)
Should not have
• cartoon look

```html
<!DOCTYPE html>
<html lang="en">
<head>
<meta charset="utf-8">
<title>Lumenwise Data Partners – Business Card</title>
<link href="https://fonts.googleapis.com/css2?family=Quicksand:wght@300;400;500;700&display=swap" rel="stylesheet">
<style>
  :root {
    --brand-blue: #0b5a8c;
    --rule-gray: #b8b8b8;
    --text-gray: #8a8a8a;
    --tagline-gray: #a6a6a6;
    --card-white: #ffffff;
    --backdrop: #e6e7e9;
  }
  * { box-sizing: border-box; margin: 0; padding: 0; }
  html, body {
    width: 1200px; height: 720px; overflow: hidden;
    background: var(--backdrop);
    font-family: "Quicksand", sans-serif;
  }
  .sheet {
    width: 1200px; height: 720px;
    display: flex; align-items: center; justify-content: center; gap: 40px;
  }
  .card {
    position: relative;
    width: 540px; height: 309px;
    background: var(--card-white);
    box-shadow: 0 2px 10px rgba(0,0,0,0.12);
  }

  /* Wordmark */
  .wordmark { display: flex; align-items: center; gap: 12px; color: var(--brand-blue); font-weight: 500; white-space: nowrap; }
  .wordmark-square { background: var(--brand-blue); flex: none; }

  /* Front */
  .card-front { display: flex; flex-direction: column; align-items: center; justify-content: center; }
  .card-front .wordmark { font-size: 34px; letter-spacing: 0.5px; }
  .card-front .wordmark-square { width: 30px; height: 30px; }
  .tagline { margin-top: 46px; font-size: 15px; font-weight: 300; color: var(--tagline-gray); letter-spacing: 1.4px; }

  /* Back */
  .card-back .wordmark { position: absolute; left: 32px; top: 38px; font-size: 19px; }
  .card-back .wordmark-square { width: 18px; height: 18px; }
  .holder {
    position: absolute; right: 32px; top: 92px;
    font-size: 19px; color: var(--brand-blue); font-weight: 700; letter-spacing: 0.6px; white-space: nowrap;
  }
  .holder-title { font-weight: 500; }
  .divider { position: absolute; left: 32px; right: 32px; top: 124px; height: 2px; display: flex; }
  .divider-gray { flex: 1; height: 1px; background: var(--rule-gray); margin-top: 1px; }
  .divider-blue { width: 215px; height: 2px; background: var(--brand-blue); }
  .contacts { position: absolute; left: 32px; top: 160px; list-style: none; }
  .contact {
    display: flex; align-items: center; gap: 12px;
    font-size: 14px; color: var(--text-gray); letter-spacing: 0.8px; line-height: 28px; white-space: nowrap;
  }
  .contact svg { width: 15px; height: 15px; fill: var(--brand-blue); flex: none; }
</style>
</head>
<body>
<main class="sheet">
  <section class="card card-front" aria-label="Card front">
    <div class="wordmark"><span class="wordmark-square"></span><span>Lumenwise Data Partners</span></div>
    <p class="tagline">Foresight is the best care</p>
  </section>

  <section class="card card-back" aria-label="Card back">
    <div class="wordmark"><span class="wordmark-square"></span><span>Lumenwise Data Partners</span></div>
    <p class="holder">Mara Feldhovenik<span class="holder-title">, PhD</span></p>
    <div class="divider"><span class="divider-gray"></span><span class="divider-blue"></span></div>
    <ul class="contacts">
      <li class="contact">
        <svg viewBox="0 0 16 16" aria-hidden="true"><path d="M3.6 1.5l2.3 2.6-1.3 1.8c.9 2 2.5 3.6 4.5 4.5l1.8-1.3 2.6 2.3-1.4 2.4C7 13.3 2.7 9 1.2 3z"/></svg>
        <span>555.283.9170</span>
      </li>
      <li class="contact">
        <svg viewBox="0 0 16 16" aria-hidden="true"><path d="M1 3.5h14v9H1z M1.8 4.3L8 9l6.2-4.7" fill="none" stroke="#0b5a8c" stroke-width="1.5"/></svg>
        <span>drmara@ourbrightmarq.com</span>
      </li>
      <li class="contact">
        <svg viewBox="0 0 16 16" aria-hidden="true"><circle cx="8" cy="8" r="6.5" fill="none" stroke="#0b5a8c" stroke-width="1.4"/><path d="M1.5 8h13M8 1.5c-3 3.5-3 9.5 0 13M8 1.5c3 3.5 3 9.5 0 13" fill="none" stroke="#0b5a8c" stroke-width="1.2"/></svg>
        <span>ourbrightmarq.com</span>
      </li>
    </ul>
  </section>
</main>
</body>
</html>
```